Executive Business Consulting for Telco Companies and Telco Start up companies

1.) Looking for an appealing and action oriented business card design.
2.)The target companies to work with start-ups and existing companies that focus on Business to Business applications
3.) For "OLRA", a Belgium based Executive consultancy company specialised in global reach starting from the centre of Europe = Brussels.
4.) Our core competence is the Go To Market in All major global regions, incl North America, Latin America, Asia, Japan, Europe and Africa.
5.) Design should be appealing to CEO, CFO and Venture Funds signalling; Expertise, Stability, Maturity and Commitment
6.) Preferred color scheme is Blue focussed and using a modern FONT.
7.) Logo design is included (uploaded)

Target Market(s)

Telecommunication Market. Companies in a B2B business model, developping services or applications to make business run more profitable

Industry/Entity Type

Business

Contact Information for Business Card

Company Name: OLRA
Name: Joris Vandekamp
Titel: Managing Director
Address: Lindelaan 58 , B-3390 Kortemeer , Belgium
Tel: + 32 471 283 915
Email: joris_vandekamp@mailbox-example.com
LinkedIn: be.profilenet-example.com/in/jorisvandekamp/

Font styles to use
Serif

Colors
0455a3
3277b5

Requirements
Must have
• Second Side Text: Global Market Entry, Driven to Results

```html
<!DOCTYPE html>
<html lang="en">
<head>
<meta charset="utf-8">
<title>OLRA Business Card</title>
<link rel="stylesheet" href="https://fonts.googleapis.com/css2?family=Exo+2:wght@400;500;600;700&display=swap">
<style>
  :root {
    --bg: #e6e6e6;
    --card-white: #ffffff;
    --navy: #0d3f8f;
    --blue-dark: #0455a3;
    --blue-light: #3277b5;
    --blue-bright: #0c74b2;
    --grey-word: #9c9ea3;
    --silver: #c9ccd2;
    --text-white: #f2f6fb;
  }
  * { margin: 0; padding: 0; box-sizing: border-box; }
  html, body {
    width: 1200px; height: 720px; overflow: hidden;
    background: var(--bg);
    font-family: "Exo 2", "Segoe UI", sans-serif;
  }
  .canvas { position: relative; width: 1200px; height: 720px; }
  .card {
    position: absolute; top: 240px;
    width: 410px; height: 240px;
    border-radius: 18px; overflow: hidden;
  }
  .card--front { left: 152px; background: var(--card-white); }
  .card--back {
    left: 638px;
    background: linear-gradient(135deg, var(--blue-bright) 0%, var(--blue-light) 40%, var(--blue-dark) 100%);
  }

  /* front */
  .brand { position: absolute; left: 24px; top: 28px; display: flex; align-items: center; gap: 12px; }
  .brand__dot { width: 74px; height: 74px; border-radius: 50%; background: var(--blue-dark); }
  .brand__name { font-size: 30px; font-weight: 700; color: var(--grey-word); letter-spacing: 1px; }

  .person { position: absolute; left: 27px; top: 125px; }
  .person__name { font-size: 15.5px; font-weight: 700; line-height: 1.15; color: var(--navy); text-transform: uppercase; }
  .person__title { font-size: 11.5px; font-weight: 600; line-height: 1.2; color: var(--blue-dark); }

  .divider { position: absolute; left: 40px; top: 166px; width: 280px; height: 1px; background: var(--blue-dark); }

  .contact {
    position: absolute; left: 25px; font-size: 12px; line-height: 14px;
    color: var(--blue-dark); display: flex; align-items: center; gap: 5px; white-space: nowrap;
  }
  .contact svg { width: 11px; height: 11px; flex: none; }
  .contact--address { top: 176px; }
  .contact--phone { top: 194px; }
  .contact--email { top: 194px; left: 152px; font-size: 11.5px; }
  .contact--web { top: 212px; }

  /* back */
  .back-mark { position: absolute; left: 0; right: 0; top: 80px; display: flex; justify-content: center; align-items: center; gap: 14px; }
  .back-mark__name { font-size: 44px; font-weight: 700; line-height: 1; color: var(--text-white); letter-spacing: 2px; }
  .back-mark__ring { width: 52px; height: 52px; border-radius: 50%; border: 4px solid var(--silver); }
  .tagline {
    position: absolute; left: 0; right: 0; top: 212px; text-align: center;
    font-size: 11.5px; font-weight: 500; color: var(--text-white); text-transform: uppercase; letter-spacing: 0.2px;
  }
</style>
</head>
<body>
<main class="canvas">
  <section class="card card--front" aria-label="Business card front">
    <div class="brand">
      <span class="brand__dot"></span>
      <span class="brand__name">OLRA</span>
    </div>

    <div class="person">
      <p class="person__name">Joris Vandekamp</p>
      <p class="person__title">Managing Director</p>
    </div>

    <span class="divider"></span>

    <p class="contact contact--address">
      <svg viewBox="0 0 16 16" fill="none" stroke="currentColor" stroke-width="1.6"><path d="M8 14s4.5-4.3 4.5-7.5a4.5 4.5 0 0 0-9 0C3.5 9.7 8 14 8 14z"/><circle cx="8" cy="6.5" r="1.6"/></svg>
      Lindelaan 58, B-3390 Kortemeer, Belgium
    </p>
    <p class="contact contact--phone">
      <svg viewBox="0 0 16 16" fill="currentColor"><path d="M3.6 1.5l2.3 2.6-1.3 1.6c.9 2 2.5 3.6 4.6 4.6l1.6-1.3 2.6 2.3-1.4 2.2C7 13.2 2.8 9 2 3z"/></svg>
      +32 471 283 915
    </p>
    <p class="contact contact--email">
      <svg viewBox="0 0 16 16" fill="currentColor"><path d="M1 3.5h14v9H1z M1.8 4.2L8 9l6.2-4.8" stroke="#fff" stroke-width="1"/></svg>
      joris_vandekamp@mailbox-example.com
    </p>
    <p class="contact contact--web">
      <svg viewBox="0 0 16 16" fill="none" stroke="currentColor" stroke-width="1.5"><circle cx="8" cy="8" r="6"/><path d="M2 8h12M8 2c2 2 2 10 0 12M8 2c-2 2-2 10 0 12"/></svg>
      be.profilenet-example.com/in/jorisvandekamp
    </p>
  </section>

  <section class="card card--back" aria-label="Business card back">
    <div class="back-mark">
      <span class="back-mark__name">OLRA</span>
      <span class="back-mark__ring"></span>
    </div>
    <p class="tagline">Global Market Entry, Driven to Results</p>
  </section>
</main>
</body>
</html>
```